Very personalised Wedding Invitation

I want a wedding invitation very unique and personalised with the menus, ceremony time table and thank you cards. I want a mix of a nice traditional style with indian style touch. I don't want a colourful invitation, it can have max. two different colours.

The bride's name is Miranda and the groom's name is Rohan

Reason: None of the designs submitted are what I am looking for

Target Market(s)

Invitations, personalised invitations,

Industry/Entity Type

Wedding

Logo Text

Our initials R&M To use in our wedding things

Font styles to use
Decorative
Script

Requirements
Must have
• -
Nice to have
• I would like a chic design with a bit of indian style
Should not have
• --

```html
<!DOCTYPE html>
<html lang="en">
<head>
<meta charset="utf-8">
<title>Miranda &amp; Rohan – Wedding Invitation</title>
<link rel="stylesheet" href="https://fonts.googleapis.com/css2?family=Dancing+Script:wght@400;500&family=Open+Sans:wght@400;700&display=swap">
<style>
  :root {
    --blush: #ef9b9c;
    --ink: #ffffff;
    --backdrop: #e6e6e6;
    --fold-shade: rgba(150, 70, 72, 0.16);
  }
  * { margin: 0; padding: 0; box-sizing: border-box; }
  html, body {
    width: 1200px;
    height: 1134px;
    overflow: hidden;
    background: var(--backdrop);
  }
  .canvas {
    position: relative;
    width: 1200px;
    height: 1134px;
  }
  .invitation-spread {
    position: absolute;
    left: 20px;
    top: 277px;
    width: 1160px;
    height: 580px;
    display: flex;
    box-shadow: 0 6px 18px rgba(0, 0, 0, 0.18);
  }
  .panel {
    position: relative;
    width: 580px;
    height: 580px;
    background: var(--blush);
    overflow: hidden;
  }
  .panel--back::after {
    content: "";
    position: absolute;
    top: 0;
    right: 0;
    width: 70px;
    height: 100%;
    background: linear-gradient(to right, rgba(0,0,0,0), var(--fold-shade));
  }
  .panel--front::before {
    content: "";
    position: absolute;
    top: 0;
    left: 0;
    width: 8px;
    height: 100%;
    background: linear-gradient(to right, var(--fold-shade), rgba(0,0,0,0));
  }
  .emblem {
    position: absolute;
    left: 227px;
    top: 227px;
    width: 128px;
    height: 128px;
    border-radius: 50%;
    background: radial-gradient(circle, rgba(255,255,255,0.55), rgba(255,255,255,0.25) 70%, rgba(255,255,255,0.1));
  }
  .mandala-edge {
    position: absolute;
    left: 380px;
    top: 93px;
    width: 400px;
    height: 400px;
    border-radius: 50%;
    background: radial-gradient(circle, rgba(255,255,255,0.5), rgba(255,255,255,0.3) 65%, rgba(255,255,255,0.15));
  }
  .couple-names {
    position: absolute;
    left: 34px;
    top: 118px;
    width: 350px;
    height: 200px;
    color: var(--ink);
    font-family: "Dancing Script", cursive;
    font-weight: 400;
    line-height: 1;
  }
  .couple-names .bride {
    position: absolute;
    left: 0;
    top: 0;
    font-size: 76px;
    white-space: nowrap;
  }
  .couple-names .ampersand {
    position: absolute;
    left: 274px;
    top: 40px;
    font-size: 66px;
  }
  .couple-names .groom {
    position: absolute;
    left: 70px;
    top: 88px;
    font-size: 76px;
    white-space: nowrap;
  }
  .divider {
    position: absolute;
    left: 188px;
    top: 342px;
  }
  .details {
    position: absolute;
    left: 0;
    top: 382px;
    width: 436px;
    text-align: center;
    color: var(--ink);
    font-family: "Open Sans", sans-serif;
  }
  .details .date,
  .details .place {
    font-weight: 700;
    font-size: 18px;
    letter-spacing: 2.4px;
    line-height: 34px;
  }
  .details .note {
    font-weight: 400;
    font-size: 13px;
    letter-spacing: 1.6px;
    margin-top: 2px;
  }
</style>
</head>
<body>
<main class="canvas">
  <section class="invitation-spread">
    <div class="panel panel--back">
      <div class="emblem" role="img" aria-label="Small white line mandala ornament"></div>
    </div>
    <div class="panel panel--front">
      <div class="mandala-edge" role="img" aria-label="Large white lace mandala ornament cut by the right edge"></div>
      <h1 class="couple-names">
        <span class="bride">Miranda</span>
        <span class="ampersand">&amp;</span>
        <span class="groom">Rohan</span>
      </h1>
      <svg class="divider" width="64" height="16" viewBox="0 0 64 16" aria-hidden="true">
        <path d="M2 8 C14 2, 24 4, 32 8 S50 14, 62 6" fill="none" stroke="#ffffff" stroke-width="3" stroke-linecap="round"/>
      </svg>
      <div class="details">
        <p class="date">8TH OF JULY 2018</p>
        <p class="place">ASHFORD HILLS, NY 10452</p>
        <p class="note">DINNER AND DANCING TO FOLLOW</p>
      </div>
    </div>
  </section>
</main>
</body>
</html>
```